wine label

Label for wine, in black and silver, format to be in PDF ,EPS, PSD Label to be split main label to have Name: Birch Tarrow family crest, dry grown, and Clare Valley
other section to have the type of wine ie: Grenache and year of harvest.
Some ideas we had our enclosed

```html
<!DOCTYPE html>
<html lang="en">
<head>
<meta charset="utf-8">
<title>Birch Tarrow Grenache 2012 – Wine Label</title>
<link rel="stylesheet" href="https://fonts.googleapis.com/css2?family=Marcellus&family=Libre+Baskerville:wght@700&display=swap">
<style>
  :root {
    --backdrop: #1b1b1c;
    --silver-light: #e6e7e8;
    --silver-mid: #cfd1d3;
    --silver-dark: #b9bcbf;
    --ink: #262626;
    --band-dark: #2a2a2b;
    --band-mid: #4a4a4c;
    --year-plate: #c9cbcd;
  }
  * { box-sizing: border-box; margin: 0; padding: 0; }
  html, body {
    width: 1174px;
    height: 1200px;
    overflow: hidden;
    background: var(--backdrop);
  }
  .canvas {
    position: relative;
    width: 1174px;
    height: 1200px;
  }
  .label {
    position: absolute;
    left: 289px;
    top: 50px;
    width: 596px;
    height: 1100px;
    background:
      repeating-linear-gradient(90deg, rgba(255,255,255,0.18) 0 1px, rgba(0,0,0,0.04) 1px 3px, rgba(255,255,255,0.08) 3px 4px),
      linear-gradient(100deg, var(--silver-dark) 0%, var(--silver-light) 35%, var(--silver-mid) 65%, var(--silver-light) 100%);
    overflow: hidden;
  }
  .brand {
    position: absolute;
    left: 0;
    right: 0;
    top: 300px;
    text-align: center;
    color: var(--ink);
    font-family: "Marcellus", serif;
  }
  .brand-name {
    font-size: 62px;
    letter-spacing: 4px;
    text-transform: uppercase;
    line-height: 1;
  }
  .brand-tagline {
    margin-top: 28px;
    font-size: 19px;
    letter-spacing: 2.5px;
    text-transform: uppercase;
  }
  .varietal {
    position: absolute;
    left: 0;
    right: 0;
    top: 808px;
    text-align: center;
    font-family: "Marcellus", serif;
    font-size: 34px;
    letter-spacing: 9px;
    color: var(--ink);
  }
  .vintage-band {
    position: absolute;
    left: 0;
    right: 0;
    top: 892px;
    height: 208px;
    background: linear-gradient(180deg, var(--band-mid) 0%, var(--band-dark) 100%);
  }
  .vintage-plate {
    position: absolute;
    left: 219px;
    top: 1008px;
    width: 158px;
    height: 40px;
    background: var(--year-plate);
    border: 2px solid var(--ink);
    outline: 2px solid var(--year-plate);
    outline-offset: 1px;
    display: flex;
    align-items: center;
    justify-content: center;
    font-family: "Libre Baskerville", serif;
    font-weight: 700;
    font-size: 22px;
    letter-spacing: 3px;
    color: var(--ink);
  }
</style>
</head>
<body>
  <main class="canvas">
    <section class="label">
      <div class="brand">
        <p class="brand-name">Birch Tarrow</p>
        <p class="brand-tagline">Family Crest, Dry Grown, and Clare Valley</p>
      </div>
      <p class="varietal">GRENACHE</p>
      <div class="vintage-band" role="img" aria-label="Dark floral pattern band"></div>
      <div class="vintage-plate">2012</div>
    </section>
  </main>
</body>
</html>
```